*** Bakery Needs a Business Card

I need a business card for my new bakery - Pine Lane Baking Dept. We make biscuits, cakes, muffins and other sweets. Our food is honest, wholesome and down to earth - i'd love this to be reflected in the design of the card. The design MUST include our logo (see the attached image - which needs to be replicated). The design should only use 2 or at most 3 colours.

Industry/Entity Type

Bakery

Requirements
Must have
• Must include my logo.
Must have a clean, simple design.
Space for my name, my title, my phone number, my facebook page (I will provide details later)
Should not have
• Must not have lots of bright colours.
Must not have any unnescassry graphics.

```html
<!DOCTYPE html>
<html lang="en">
<head>
<meta charset="utf-8">
<title>Pine Lane Baking Dept – Business Card</title>
<link href="https://fonts.googleapis.com/css2?family=Crimson+Text:wght@400;600;700&family=Open+Sans:wght@400&display=swap" rel="stylesheet">
<style>
  :root {
    --bg: #e4e2df;
    --card: #ffffff;
    --brown: #6b4a36;
    --brown-text: #7a5a44;
    --ink: #1f1a17;
    --grey: #555555;
    --band-text: #f4ece4;
  }
  * { box-sizing: border-box; margin: 0; padding: 0; }
  html, body {
    width: 1200px; height: 951px; overflow: hidden;
    background: var(--bg);
  }
  .canvas { position: relative; width: 1200px; height: 951px; }

  .card {
    position: absolute;
    width: 700px; height: 400px;
    background: var(--card);
    border-radius: 26px;
    overflow: hidden;
    box-shadow: 0 6px 18px rgba(0,0,0,.18);
  }
  .card--front { left: 90px; top: 50px; }
  .card--back  { left: 410px; top: 500px; }

  /* Front */
  .brand-mark {
    position: absolute; left: 70px; top: 95px;
    display: flex; align-items: center; gap: 22px;
  }
  .brand-mark__square {
    width: 46px; height: 46px; background: var(--brown);
  }
  .brand-mark__name {
    font-family: "Crimson Text", serif;
    font-weight: 600;
    font-size: 96px;
    letter-spacing: 2px;
    color: var(--brown);
    line-height: 1;
  }
  .tagline-band {
    position: absolute; left: 0; right: 0; top: 322px; height: 30px;
    background: var(--brown);
    display: flex; align-items: center; justify-content: flex-end;
    padding-right: 30px;
  }
  .tagline {
    font-family: "Crimson Text", serif;
    font-size: 17px; letter-spacing: .6px;
    color: var(--band-text);
  }

  /* Back */
  .company {
    position: absolute; left: 62px; top: 48px;
    font-family: "Crimson Text", serif;
    font-size: 38px; line-height: 1.05;
    color: var(--brown-text);
  }
  .person { position: absolute; left: 428px; top: 84px; }
  .person__name {
    font-family: "Crimson Text", serif; font-weight: 700;
    font-size: 24px; color: var(--ink);
  }
  .person__title {
    font-family: "Open Sans", sans-serif;
    font-size: 14px; color: var(--grey); margin-top: 4px;
  }
  .contact {
    position: absolute; left: 62px; top: 318px;
    font-family: "Open Sans", sans-serif;
    font-size: 17px; color: var(--ink);
    display: flex; align-items: center; gap: 14px;
  }
  .contact__dot { width: 6px; height: 6px; border-radius: 50%; background: var(--ink); }
  .base-band {
    position: absolute; left: 0; right: 0; bottom: 0; height: 22px;
    background: var(--brown);
  }
</style>
</head>
<body>
<div class="canvas">
  <section class="card card--front">
    <div class="brand-mark">
      <span class="brand-mark__square"></span>
      <span class="brand-mark__name">PINE LANE</span>
    </div>
    <div class="tagline-band">
      <p class="tagline">BISCUITS, CAKES, MUFFINS AND OTHER SWEETS</p>
    </div>
  </section>

  <section class="card card--back">
    <h1 class="company">Pine Lane<br>Baking Dept</h1>
    <div class="person">
      <p class="person__name">Mark Ellison</p>
      <p class="person__title">Owner</p>
    </div>
    <p class="contact">
      <span>ph. 512-555-0143</span>
      <span class="contact__dot"></span>
      <span>www.pinelanebakes.com</span>
    </p>
    <div class="base-band"></div>
  </section>
</div>
</body>
</html>
```